Magnetic Business card Design do a service provider

Hi,

The company aim is to provide all service needs under one roof. However, at the moment there is only Accounting, Electrical and IT branches. There will be more services coming onboard in the future.

I already have a logo designed (Company name is already part of the logo), I now need a magnetic business card designed.

The business card will contain the following:

- Company Logo
- Contact#
- E-mail
- enough space to add website URL (for future)
Updates

Project Deadline Extended Reason: HI All,The deadline has been extended due to not having enough time to review an overwhelming number of designs that has been submitted by lots of designers.I will be uploading a draft of designs that i have in mind.Thanks. Added Friday, January 22, 2016

Target Market(s)

Residential, Home-based Businesses, Small and Medium businesses

Industry/Entity Type

Business

Contact Information for Business Card

Contact#: 0491 738 552
E-mail: service@brightharborgroup.net.au

Font styles to use
Decorative
Script

Requirements
Must have
• Round edges
• Some form of logo incorporation as a background

```html
<!DOCTYPE html>
<html lang="en">
<head>
<meta charset="utf-8">
<title>Bright Harbor Group – Business Card</title>
<link rel="stylesheet" href="https://fonts.googleapis.com/css2?family=Open+Sans:wght@400;600&family=Arimo:wght@400&display=swap">
<style>
  :root {
    --page: #e4e2df;
    --card: #1b1c1e;
    --card-edge: #111214;
    --blue: #1f6fc1;
    --white: #f2f2f2;
    --grey: #9a9c9f;
    --divider: #6d6f72;
    --card-w: 520px;
    --card-h: 300px;
    --radius: 16px;
  }
  * { box-sizing: border-box; margin: 0; padding: 0; }
  html, body { width: 1200px; height: 787px; overflow: hidden; }
  body {
    background: var(--page);
    display: flex;
    align-items: center;
    justify-content: center;
    gap: 56px;
    font-family: "Arimo", Arial, sans-serif;
  }
  .card {
    width: var(--card-w);
    height: var(--card-h);
    border-radius: var(--radius);
    background: var(--card);
    box-shadow: 0 0 0 1px var(--card-edge);
    position: relative;
    overflow: hidden;
    color: var(--white);
  }

  /* Back side */
  .card-back {
    background:
      radial-gradient(circle at 62% 50%, rgba(70,80,90,0.35) 0, rgba(70,80,90,0.12) 38%, rgba(0,0,0,0) 60%),
      var(--card);
  }
  .card-back .backdrop {
    position: absolute;
    inset: 0;
  }
  .card-back .web-address {
    position: absolute;
    left: 70px;
    top: 132px;
    font-family: "Open Sans", Arial, sans-serif;
    font-size: 17px;
    letter-spacing: 1.6px;
    color: var(--white);
  }

  /* Front side */
  .card-front {
    display: flex;
    align-items: center;
    padding: 0 34px 0 38px;
  }
  .brand {
    width: 200px;
    display: flex;
    align-items: center;
    gap: 10px;
  }
  .brand-dot {
    width: 14px;
    height: 14px;
    border-radius: 50%;
    background: var(--blue);
    flex: none;
  }
  .brand-name {
    font-family: "Open Sans", Arial, sans-serif;
    font-weight: 400;
    font-size: 22px;
    line-height: 1.15;
    color: var(--white);
  }
  .divider {
    width: 1px;
    height: 120px;
    background: var(--divider);
    margin: 0 22px 0 14px;
  }
  .details { flex: 1; }
  .person-name {
    font-family: "Open Sans", Arial, sans-serif;
    font-weight: 600;
    font-size: 17px;
    color: var(--blue);
  }
  .person-role {
    font-size: 13px;
    color: var(--white);
    margin-bottom: 14px;
  }
  .contact-list { list-style: none; }
  .contact-item {
    display: flex;
    align-items: center;
    gap: 10px;
    font-size: 12.5px;
    line-height: 22px;
    color: var(--white);
    white-space: nowrap;
  }
  .contact-item svg {
    width: 13px;
    height: 13px;
    fill: var(--blue);
    flex: none;
  }
</style>
</head>
<body>
  <section class="card card-back" aria-label="Card back">
    <div class="backdrop" role="img" aria-label="Faint background brand decoration area"></div>
    <p class="web-address">brightharborgroup.net.au</p>
  </section>

  <section class="card card-front" aria-label="Card front">
    <div class="brand">
      <span class="brand-dot"></span>
      <span class="brand-name">Bright Harbor Group</span>
    </div>
    <div class="divider"></div>
    <div class="details">
      <p class="person-name">Liam Carter</p>
      <p class="person-role">President</p>
      <ul class="contact-list">
        <li class="contact-item">
          <svg viewBox="0 0 16 16" aria-hidden="true"><path d="M3.5 1.5l2.5 0 1 3.5-1.6 1.2a9 9 0 0 0 4.4 4.4l1.2-1.6 3.5 1v2.5c0 .8-.7 1.5-1.5 1.5A12.5 12.5 0 0 1 2 3c0-.8.7-1.5 1.5-1.5z"/></svg>
          0491 738 552
        </li>
        <li class="contact-item">
          <svg viewBox="0 0 16 16" aria-hidden="true"><path d="M1 3.5h14v9H1z M1.5 4l6.5 5 6.5-5" stroke="#1b1c1e" stroke-width="1"/></svg>
          service@brightharborgroup.net.au
        </li>
        <li class="contact-item">
          <svg viewBox="0 0 16 16" aria-hidden="true"><circle cx="8" cy="8" r="7"/><path d="M1 8h14M8 1c-3 3.5-3 10.5 0 14M8 1c3 3.5 3 10.5 0 14" stroke="#1b1c1e" stroke-width="1" fill="none"/></svg>
          www.brightharborgroup.net.au
        </li>
      </ul>
    </div>
  </section>
</body>
</html>
```